Road Construction Company needs business cards

We would like a new business card designed for our business.

We're a road construction company based in Qld, Australia.

Can the business card please have the following information on it.

Name: Brent Malvoy
Position: General Manager
Phone: 0471 592 304
Email: Brent.malvoy@quendix.com.au
Address: 87 Harrowgate Ave, Pindarra, QLD, 4000
Website: www.quendix.com.au

Visually we'd like the card to be professional and simple.

Attached is our logo.

Our website is www.quendix.com.au

Target Market(s)

Men aged 25-60

Contact Information for Business Card

As listed in project description

Font styles to use
Serif

Requirements
Must have
• Large logo on back of card

```html
<!DOCTYPE html>
<html lang="en">
<head>
<meta charset="utf-8">
<title>Quendix Business Card</title>
<link rel="stylesheet" href="https://fonts.googleapis.com/css2?family=Outfit:wght@400;600;800&display=swap">
<style>
  :root {
    --backdrop: #34a4d8;
    --card: #ffffff;
    --navy: #0452a0;
    --ink-light: #ffffff;
    --shadow: rgba(0, 40, 80, 0.28);
  }
  * { margin: 0; padding: 0; box-sizing: border-box; }
  html, body {
    width: 1200px; height: 1000px; overflow: hidden;
    background: var(--backdrop);
    font-family: "Outfit", sans-serif;
  }
  .stage { position: relative; width: 1200px; height: 1000px; }
  .card {
    position: absolute; left: 233px; width: 735px; height: 420px;
    background: var(--card);
    box-shadow: 4px 5px 8px var(--shadow);
    overflow: hidden;
  }
  .card--back { top: 62px; }
  .card--front { top: 518px; }

  .wordmark {
    color: var(--navy); font-weight: 800; letter-spacing: 0.04em;
    text-transform: uppercase; line-height: 1;
  }
  .card--back .wordmark {
    position: absolute; left: 0; right: 0; top: 158px;
    text-align: center; font-size: 96px;
  }

  .front-panel { position: absolute; inset: 0; width: 100%; height: 100%; }
  .identity { position: absolute; left: 37px; top: 52px; color: var(--ink-light); }
  .identity__name { font-size: 31px; font-weight: 600; letter-spacing: 0.03em; line-height: 1.1; }
  .identity__role { font-size: 21px; font-weight: 400; letter-spacing: 0.06em; margin-top: 4px; margin-left: 2px; }

  .contacts { position: absolute; left: 36px; top: 172px; list-style: none; color: var(--ink-light); }
  .contacts__item {
    display: flex; align-items: center; height: 36px; margin-bottom: 16px;
    font-size: 18.5px; letter-spacing: 0.04em; text-transform: uppercase;
  }
  .contacts__icon { width: 22px; height: 22px; margin-right: 18px; fill: var(--ink-light); flex: none; }

  .card--front .wordmark {
    position: absolute; left: 466px; top: 330px; font-size: 40px;
  }
</style>
</head>
<body>
<main class="stage">
  <section class="card card--back" aria-label="Card back">
    <div class="wordmark">Quendix</div>
  </section>

  <section class="card card--front" aria-label="Card front">
    <svg class="front-panel" viewBox="0 0 735 420" preserveAspectRatio="none" aria-hidden="true">
      <polygon points="0,0 628,0 373,420 0,420" fill="var(--navy)"/>
    </svg>

    <div class="identity">
      <p class="identity__name">BRENT MALVOY</p>
      <p class="identity__role">GENERAL MANAGER</p>
    </div>

    <ul class="contacts">
      <li class="contacts__item">
        <svg class="contacts__icon" viewBox="0 0 24 24" aria-hidden="true"><path d="M12 1.5a8 8 0 0 0-8 8c0 6 8 13 8 13s8-7 8-13a8 8 0 0 0-8-8zm0 11a3 3 0 1 1 0-6 3 3 0 0 1 0 6z"/></svg>
        87 Harrowgate Ave, Pindarra, QLD, 4000
      </li>
      <li class="contacts__item">
        <svg class="contacts__icon" viewBox="0 0 24 24" aria-hidden="true"><path d="M6.6 2.5l3 3.6-2 2.4a13 13 0 0 0 7.9 7.9l2.4-2 3.6 3-1.8 3.1C12 21 3 12 3.5 4.3z"/></svg>
        0471 592 304
      </li>
      <li class="contacts__item">
        <svg class="contacts__icon" viewBox="0 0 24 24" aria-hidden="true"><path d="M2 5h20v14H2zm2 2v.4l8 6 8-6V7zm0 2.9V17h16V9.9l-8 6z"/></svg>
        Brent.malvoy@quendix.com.au
      </li>
      <li class="contacts__item">
        <svg class="contacts__icon" viewBox="0 0 24 24" aria-hidden="true"><path d="M12 2a10 10 0 1 0 0 20 10 10 0 0 0 0-20zm0 2a8 8 0 0 1 7.9 7H4.1A8 8 0 0 1 12 4zm-7.9 9h15.8A8 8 0 0 1 4.1 13z"/></svg>
        www.quendix.com.au
      </li>
    </ul>

    <div class="wordmark">Quendix</div>
  </section>
</main>
</body>
</html>
```